New Personal Trainer needs poster to attract clients

Hi I am a personal trainer working inside a busy gym. My sole base of clients is from the gym itself where I compete with other trainers for business.
New company so my brand is still not noticed by the public.
My company name is Stridewell PT.
I am looking for a poster that will attract attention and increase awareness of my brand. My market will be mostly overweight men/women aged from 25-55 years old.
I would like pics of some sort on there that would be appropriate for my target market. Design needs to be colorful to attract attention.

My name and number must be added as well as facebook details
Dean Harlow
0437290518
(Facebook Symbol) Dean Harlow PT

Target Market(s)

Overweight men and women aged 25-55 years. Some would be mothers with young children

Industry/Entity Type

Fitness

Font styles to use
Sans Serif

Requirements
Must have
• My Logo.
• Pictures.
• Bright Attractive colours
• My name and number
• Slogan
Nice to have
• Slogan I'm leaning towards is "Building a Better You" but open to any ideas with this.

```html
<!DOCTYPE html>
<html lang="en">
<head>
<meta charset="utf-8">
<title>Stridewell PT Poster</title>
<link rel="stylesheet" href="https://fonts.googleapis.com/css2?family=Anton&family=Archivo+Black&family=Roboto:wght@400&family=Tinos&display=swap">
<style>
  :root {
    --backdrop: #c9c9c9;
    --poster: #000000;
    --yellow: #f7d417;
    --blue: #0a7fc8;
    --navy: #1d3a52;
    --white: #ffffff;
    --photo-light: #3b3d40;
    --photo-dark: #0b0b0c;
    --badge: #3b5a9a;
  }
  html, body {
    margin: 0;
    width: 1200px;
    height: 1200px;
    overflow: hidden;
    background: var(--backdrop);
  }
  .poster {
    position: absolute;
    left: 237px;
    top: 127px;
    width: 726px;
    height: 946px;
    background: var(--poster);
    overflow: hidden;
  }
  .stripes { position: absolute; }
  .stripes--top-left { left: 0; top: 77px; }
  .stripes--top-right { left: 594px; top: 77px; }
  .stripes--bottom-left { left: 0; top: 713px; }
  .stripes--bottom-right { left: 600px; top: 713px; }
  .brand-name {
    position: absolute;
    left: 124px;
    width: 462px;
    top: 72px;
    text-align: center;
    font-family: "Archivo Black", sans-serif;
    font-size: 47px;
    line-height: 64px;
    color: var(--yellow);
    white-space: nowrap;
  }
  .hero-photo {
    position: absolute;
    left: 0;
    top: 169px;
    width: 726px;
    height: 540px;
    background:
      radial-gradient(ellipse at 45% 55%, var(--photo-light) 0%, #1c1d1f 45%, var(--photo-dark) 80%);
  }
  .speed-lines { position: absolute; left: 50px; top: 575px; }
  .slogan {
    position: absolute;
    margin: 0;
    font-family: "Anton", sans-serif;
    font-weight: 400;
    text-transform: uppercase;
    line-height: 1;
    white-space: nowrap;
    text-shadow: 3px 4px 6px rgba(0,0,0,0.7);
  }
  .slogan--first {
    left: 52px;
    top: 452px;
    font-size: 104px;
    color: var(--yellow);
    transform: rotate(-7deg) scaleX(0.82);
    transform-origin: left top;
  }
  .slogan--second {
    left: 258px;
    top: 560px;
    font-size: 104px;
    color: var(--blue);
    transform: rotate(-7deg) scaleX(0.82);
    transform-origin: left top;
  }
  .trainer-name {
    position: absolute;
    left: 0;
    width: 726px;
    top: 718px;
    text-align: center;
    font-family: "Tinos", serif;
    font-size: 57px;
    line-height: 62px;
    color: var(--blue);
    letter-spacing: 1px;
  }
  .trainer-phone {
    position: absolute;
    left: 0;
    width: 726px;
    top: 766px;
    text-align: center;
    font-family: "Tinos", serif;
    font-size: 92px;
    line-height: 92px;
    color: var(--white);
  }
  .social {
    position: absolute;
    left: 175px;
    top: 857px;
    display: flex;
    align-items: center;
    gap: 10px;
  }
  .social__dot {
    width: 32px;
    height: 32px;
    border-radius: 50%;
    background: var(--badge);
  }
  .social__handle {
    font-family: "Roboto", sans-serif;
    font-size: 29px;
    color: var(--yellow);
    text-transform: uppercase;
  }
</style>
</head>
<body>
  <main class="poster">
    <svg class="stripes stripes--top-left" width="116" height="58" aria-hidden="true">
      <rect x="0" y="0" width="116" height="9" fill="var(--blue)"/>
      <rect x="0" y="16" width="116" height="9" fill="var(--blue)"/>
      <rect x="0" y="32" width="116" height="9" fill="var(--blue)"/>
      <rect x="0" y="48" width="116" height="9" fill="var(--blue)"/>
    </svg>
    <div class="brand-name">STRIDEWELL PT</div>
    <svg class="stripes stripes--top-right" width="132" height="58" aria-hidden="true">
      <rect x="0" y="0" width="132" height="9" fill="var(--yellow)"/>
      <rect x="0" y="16" width="132" height="9" fill="var(--yellow)"/>
      <rect x="0" y="32" width="132" height="9" fill="var(--yellow)"/>
      <rect x="0" y="48" width="132" height="9" fill="var(--yellow)"/>
    </svg>

    <div class="hero-photo" role="img" aria-label="Close-up photo of a chalked hand gripping a barbell, with chalk dust in the air and a trainer shoe behind"></div>

    <svg class="speed-lines" width="210" height="70" aria-hidden="true">
      <path d="M0 38 L205 6 L205 10 Z" fill="var(--white)"/>
      <path d="M10 50 L205 22 L205 27 Z" fill="var(--white)"/>
      <path d="M70 66 L205 42 L205 46 Z" fill="var(--white)"/>
    </svg>
    <p class="slogan slogan--first">"Building a</p>
    <p class="slogan slogan--second">Better You"</p>

    <svg class="stripes stripes--bottom-left" width="126" height="190" aria-hidden="true">
      <defs>
        <linearGradient id="fadeBlue" x1="0" x2="1" y1="0" y2="0">
          <stop offset="0" stop-color="var(--blue)"/>
          <stop offset="1" stop-color="var(--blue)" stop-opacity="0"/>
        </linearGradient>
        <linearGradient id="fadeNavy" x1="0" x2="1" y1="0" y2="0">
          <stop offset="0" stop-color="var(--navy)"/>
          <stop offset="1" stop-color="var(--navy)" stop-opacity="0"/>
        </linearGradient>
      </defs>
      <rect x="0" y="0" width="126" height="7" fill="url(#fadeBlue)"/>
      <rect x="0" y="14" width="126" height="7" fill="url(#fadeBlue)"/>
      <rect x="0" y="28" width="126" height="7" fill="url(#fadeBlue)"/>
      <rect x="0" y="42" width="126" height="7" fill="url(#fadeBlue)"/>
      <rect x="0" y="56" width="126" height="7" fill="url(#fadeNavy)"/>
      <rect x="0" y="70" width="126" height="7" fill="url(#fadeNavy)"/>
      <rect x="0" y="84" width="126" height="7" fill="url(#fadeNavy)"/>
      <rect x="0" y="98" width="126" height="7" fill="url(#fadeNavy)"/>
      <rect x="0" y="112" width="126" height="7" fill="url(#fadeNavy)"/>
      <rect x="0" y="126" width="126" height="7" fill="url(#fadeNavy)"/>
      <rect x="0" y="140" width="126" height="7" fill="url(#fadeNavy)"/>
      <rect x="0" y="154" width="126" height="7" fill="url(#fadeNavy)"/>
      <rect x="0" y="168" width="126" height="7" fill="url(#fadeNavy)"/>
      <rect x="0" y="182" width="126" height="7" fill="url(#fadeNavy)"/>
    </svg>
    <svg class="stripes stripes--bottom-right" width="126" height="190" aria-hidden="true">
      <defs>
        <linearGradient id="fadeYellowR" x1="1" x2="0" y1="0" y2="0">
          <stop offset="0" stop-color="var(--yellow)"/>
          <stop offset="1" stop-color="var(--yellow)" stop-opacity="0"/>
        </linearGradient>
        <linearGradient id="fadeNavyR" x1="1" x2="0" y1="0" y2="0">
          <stop offset="0" stop-color="var(--navy)"/>
          <stop offset="1" stop-color="var(--navy)" stop-opacity="0"/>
        </linearGradient>
      </defs>
      <rect x="0" y="0" width="126" height="7" fill="url(#fadeYellowR)"/>
      <rect x="0" y="14" width="126" height="7" fill="url(#fadeYellowR)"/>
      <rect x="0" y="28" width="126" height="7" fill="url(#fadeYellowR)"/>
      <rect x="0" y="42" width="126" height="7" fill="url(#fadeYellowR)"/>
      <rect x="0" y="56" width="126" height="7" fill="url(#fadeNavyR)"/>
      <rect x="0" y="70" width="126" height="7" fill="url(#fadeNavyR)"/>
      <rect x="0" y="84" width="126" height="7" fill="url(#fadeNavyR)"/>
      <rect x="0" y="98" width="126" height="7" fill="url(#fadeNavyR)"/>
      <rect x="0" y="112" width="126" height="7" fill="url(#fadeNavyR)"/>
      <rect x="0" y="126" width="126" height="7" fill="url(#fadeNavyR)"/>
      <rect x="0" y="140" width="126" height="7" fill="url(#fadeNavyR)"/>
      <rect x="0" y="154" width="126" height="7" fill="url(#fadeNavyR)"/>
      <rect x="0" y="168" width="126" height="7" fill="url(#fadeNavyR)"/>
      <rect x="0" y="182" width="126" height="7" fill="url(#fadeNavyR)"/>
    </svg>

    <div class="trainer-name">DEAN HARLOW</div>
    <div class="trainer-phone">0437290518</div>
    <div class="social">
      <span class="social__dot" aria-hidden="true"></span>
      <span class="social__handle">Dean Harlow PT</span>
    </div>
  </main>
</body>
</html>
```